Bright Towns Alliance PowerPoint Design Template and Sample Deck

The Bright Towns Alliance is an international organization that seeks to improve the livability, workability and sustainability of the world’s cities.
We seek a versatile PowerPoint design template with 10 slide types plus a “self-documenting” sample deck. Your design will be used in keynote speeches and workshops around the world.
After the contest is completed, we will ask the winning designer to add 10-20 additional slide types for $75 per slide. We also seek a long-term relationship whereby we can request “custom” slides and/or ask the designer to touch up the slides we build to make them better.
FILES. We have uploaded several files:
1. BRIGHT TOWNS ALLIANCE DESIGN CONTEST NOTES.docx with full instructions.
2. PALETTE. Shows our official colors.
3 LOGOS. Several individual files with different variations of our logo. Some with our motto, some without.
2. SAMPLE SLIDES. Because we were unable to successfully upload our sample deck, we are making it available via this FileCrate link:
https://www.filecrate-example.net/s/k7qvmr2tn8wzd4h/The%20Bright%20Towns%20Alliance%20Design%20Contest%20Notes.docx?dl=0
Target Market(s)
Mayors, department heads, CIOs, senior executives from technology companies
Industry/Entity Type
Information Technology
Colors
Designer to choose colors to be used in the design.
Requirements
Must have
- Please see uploaded Word document for requirements, nice to haves and should not haves and uploaded palette for color preferences.
Nice to have
- see above
Should not have
- see above

```html
<!DOCTYPE html>
<html lang="en">
<head>
<meta charset="utf-8">
<title>Bright Towns Alliance – Sample Deck Slides</title>
<link rel="stylesheet" href="https://fonts.googleapis.com/css2?family=Carlito:ital,wght@0,400;0,700;1,700&display=swap">
<style>
  :root {
    --stage-grey: #636363;
    --navy: #002a56;
    --orange: #f7952f;
    --orange-dark: #d8832a;
    --arrow-grey: #7b7c7e;
    --arrow-grey-dark: #5f6062;
    --white: #ffffff;
    --ink: #1e1e1e;
  }
  * { margin: 0; padding: 0; box-sizing: border-box; }
  html, body {
    width: 1200px; height: 960px; overflow: hidden;
    background: var(--stage-grey);
    font-family: "Carlito", "Calibri", sans-serif;
  }
  .deck { position: relative; width: 1200px; height: 960px; }
  .slide { position: absolute; display: block; background: var(--navy); }
  .slide--process { left: 96px; top: 89px; width: 480px; height: 270px; }
  .slide--contact { left: 628px; top: 89px; width: 480px; height: 270px; }
  .slide--questions { left: 183px; top: 398px; width: 833px; height: 468px; }
  .slide-bg { fill: var(--navy); }
  .title { fill: var(--orange); font-weight: 700; }
  .subtitle { fill: var(--white); font-weight: 700; font-style: italic; font-size: 8px; }
  .step-label { fill: var(--white); font-weight: 700; font-size: 5px; letter-spacing: 1.2px; }
  .step-text { fill: var(--white); font-weight: 700; font-size: 5.6px; }
  .step-num { fill: var(--ink); font-weight: 700; font-size: 8px; }
  .contact-label { fill: var(--orange); font-weight: 700; font-size: 5px; letter-spacing: 1.2px; }
  .contact-text { fill: var(--orange); font-weight: 700; font-size: 5.3px; }
  .icon-box { fill: none; stroke: var(--arrow-grey); stroke-width: 1; }
  .icon { fill: none; stroke: var(--orange); stroke-width: 1.3; stroke-linejoin: round; }
  .page-tab { fill: var(--orange); }
  .page-num { fill: var(--ink); font-weight: 700; text-anchor: middle; }
  .questions-title { fill: var(--orange); font-size: 68px; letter-spacing: 3px; text-anchor: middle; }
</style>
</head>
<body>
<main class="deck">

  <!-- Slide 13: linear process -->
  <svg class="slide slide--process" viewBox="0 0 600 338" xmlns="http://www.w3.org/2000/svg">
    <rect class="slide-bg" width="600" height="338"/>
    <text class="title" x="300" y="52" text-anchor="middle" font-size="20">LINEAR PROCESS  sample 1</text>
    <text class="subtitle" x="300" y="78" text-anchor="middle">Sed ut perspiciatis unde omnis iste natus error sit voluptatem</text>

    <polygon fill="var(--arrow-grey-dark)" points="101,266 172,266 300,128 228,128"/>
    <polygon fill="var(--arrow-grey)" points="300,128 335,128 335,116 365,146 335,176 335,164 300,164 284,146"/>
    <polygon fill="var(--arrow-grey)" points="255,170 290,170 290,158 322,188 290,218 290,206 255,206 240,188"/>
    <polygon fill="var(--orange-dark)" points="101,266 172,266 210,213 139,213"/>
    <polygon fill="var(--orange)" points="175,213 250,213 250,201 278,231 250,261 250,249 175,249 192,231"/>
    <text class="step-num" x="321" y="149" text-anchor="middle" fill="#fff" style="fill:#fff">3</text>
    <text class="step-num" x="275" y="191" text-anchor="middle" style="fill:#fff">2</text>
    <text class="step-num" x="226" y="234" text-anchor="middle">1</text>

    <text class="step-label" x="396" y="141">TITLE HERE</text>
    <text class="step-text" x="396" y="157">lorem ipsum dolor sit amet</text>
    <text class="step-text" x="396" y="167">aleh pue hom hai nyang</text>
    <text class="step-text" x="396" y="177">penting olah dan</text>

    <text class="step-label" x="349" y="196">TITLE HERE</text>
    <text class="step-text" x="349" y="212">lorem ipsum dolor sit amet</text>
    <text class="step-text" x="349" y="222">aleh pue hom hai nyang</text>
    <text class="step-text" x="349" y="232">penting olah dan</text>

    <text class="step-label" x="297" y="244">TITLE HERE</text>
    <text class="step-text" x="297" y="260">lorem ipsum dolor sit amet</text>
    <text class="step-text" x="297" y="270">aleh pue hom hai nyang</text>
    <text class="step-text" x="297" y="280">penting olah dan</text>

    <polygon class="page-tab" points="281,338 299,320 317,338"/>
    <text class="page-num" x="299" y="334" font-size="6">13</text>
  </svg>

  <!-- Slide 14: get in touch -->
  <svg class="slide slide--contact" viewBox="0 0 600 338" xmlns="http://www.w3.org/2000/svg">
    <defs>
      <linearGradient id="phone-fill" x1="0" y1="0" x2="0" y2="1">
        <stop offset="0" stop-color="#d9d9d9"/>
        <stop offset="1" stop-color="#bdbdbd"/>
      </linearGradient>
    </defs>
    <rect class="slide-bg" width="600" height="338"/>
    <rect x="66" y="30" width="137" height="288" rx="20" fill="url(#phone-fill)" role="img" aria-label="Smartphone showing a close-up photo of a keyboard key with an envelope symbol"/>

    <text class="title" x="405" y="73" text-anchor="middle" font-size="31">GET IN TOUCH</text>

    <rect class="icon-box" x="293" y="125" width="40" height="40"/>
    <path class="icon" d="M313 135 a6 6 0 0 1 6 6 c0 5 -6 12 -6 12 c0 0 -6 -7 -6 -12 a6 6 0 0 1 6 -6z"/>
    <circle class="icon" cx="313" cy="141" r="2"/>
    <text class="contact-label" x="356" y="129">ADDRESS</text>
    <text class="contact-text" x="356" y="140">Lorem ipsum dolor sit amet, consectetur adipiscing elit, sed do</text>
    <text class="contact-text" x="356" y="150">eiusmod tempor incididunt ut labore et dolore magna aliqua. Ut</text>
    <text class="contact-text" x="356" y="160">enim. nostrud exercitation ullamco laboris nisi ut</text>

    <rect class="icon-box" x="293" y="184" width="40" height="40"/>
    <rect class="icon" x="308" y="193" width="10" height="21" rx="1.5"/>
    <line class="icon" x1="308" y1="197" x2="318" y2="197"/>
    <line class="icon" x1="308" y1="210" x2="318" y2="210"/>
    <text class="contact-label" x="356" y="188">CONTACT</text>
    <text class="contact-text" x="356" y="201">Lorem ipsum dolor sit amet, consectetur adipiscing elit, sed do</text>
    <text class="contact-text" x="356" y="211">eiusmod tempor incididunt ut labore et dolore magna aliqua. Ut</text>
    <text class="contact-text" x="356" y="221">enim. nostrud exercitation ullamco laboris nisi ut</text>

    <rect class="icon-box" x="293" y="246" width="40" height="40"/>
    <rect class="icon" x="304" y="260" width="18" height="12"/>
    <polyline class="icon" points="304,260 313,267 322,260"/>
    <text class="contact-label" x="356" y="250">EMAIL</text>
    <text class="contact-text" x="356" y="264">Lorem ipsum dolor sit amet, consectetur adipiscing elit, sed do</text>
    <text class="contact-text" x="356" y="274">eiusmod tempor incididunt ut labore et dolore magna aliqua. Ut</text>
    <text class="contact-text" x="356" y="284">enim. nostrud exercitation ullamco laboris nisi ut</text>

    <polygon class="page-tab" points="273,338 291,320 309,338"/>
    <text class="page-num" x="291" y="334" font-size="6">14</text>
  </svg>

  <!-- Slide 15: any questions -->
  <svg class="slide slide--questions" viewBox="0 0 1041 585" xmlns="http://www.w3.org/2000/svg">
    <rect class="slide-bg" width="1041" height="585"/>
    <circle cx="521" cy="199" r="73" fill="var(--orange)"/>
    <ellipse cx="526" cy="192" rx="40" ry="28" fill="var(--white)"/>
    <path d="M500 208 L492 238 L520 216 Z" fill="var(--white)"/>
    <line x1="292" y1="302" x2="751" y2="302" stroke="var(--orange)" stroke-width="4"/>
    <text class="questions-title" x="521" y="370">ANY QUESTIONS?</text>
    <polygon class="page-tab" points="261,585 296,548 331,585"/>
    <text class="page-num" x="296" y="578" font-size="10">15</text>
  </svg>

</main>
</body>
</html>
```